A book about police officer shootings needs a dynamic cover design

I've almost completed a book on officer involved shootings...a very hot topic today. The title is "R.K.T. Beyond The Silence Fell." (emphasis on "beyond the silence") It details three separate shooting incidents, all within the same law enforcement family.I need a professional looking book cover that helps capture the drama. I attached a file of something I put together that is close, but I am concerned about "readability" and want a more professional look. I included a photo that I took off the internet of a gun being shot. That particular photo can stay or go, or be altered, but I like the perspective of the photo being fired from the person behind it. I wanted the cover to have the characteristics and color of a police uniform, utilizing blues, silvers, and maybe a little gold. I'm concerned about making sure the font and colors are also easy to read. I also will be working on a website design for "Beyond The Silence.Com" once the book hits the market. The back cover will incorporate the same colors, but only be a picture and excerpts from the book. I've included both for your review.

Target Market(s)

Law Enforcement, Christian, Media

Font styles to use
Sans Serif

Requirements
Must have
• A professional and readable appearance, that captures the drama of the topic. All the wording on the sample cover I attached, unless you come up with something better. A gun being fired from the perspective of the officer pulling the trigger. The size of the book will be the standard 6 x 9 in size. "Beyond The Silence" will eventually be my website domain and social media promotion hashtag.
Nice to have
• I would like the cover to incorporate the colors of a police uniform and badge, traditionally, navy blue, silver and some gold.
Should not have
• No police badge with a black band across. Not my topic.

```html
<!DOCTYPE html>
<html lang="en">
<head>
<meta charset="utf-8">
<title>R.K.T. Beyond the Silence Fell — Book Cover</title>
<link href="https://fonts.googleapis.com/css2?family=Michroma&family=Questrial&display=swap" rel="stylesheet">
<style>
  :root {
    --backdrop-deep: #2a0b5a;
    --backdrop-warm: #f27a0c;
    --cover-navy: #0d1230;
    --cover-violet: #6a6aa8;
    --cover-lavender: #b6b4dc;
    --cover-red: #9a1414;
    --cover-magenta: #c2306a;
    --text-white: #ffffff;
    --band-dark: rgba(10, 10, 24, 0.82);
  }
  html, body {
    margin: 0;
    padding: 0;
    width: 1200px;
    height: 1000px;
    overflow: hidden;
  }
  .stage {
    position: relative;
    width: 1200px;
    height: 1000px;
    background:
      radial-gradient(ellipse 70% 55% at 50% 105%, var(--backdrop-warm) 0%, #b2461f 30%, #5a1a48 60%, transparent 85%),
      var(--backdrop-deep);
    overflow: hidden;
  }
  .book-cover {
    position: absolute;
    left: 302px;
    top: 42px;
    width: 623px;
    height: 935px;
    overflow: hidden;
    color: var(--text-white);
  }
  .cover-art {
    position: absolute;
    inset: 0;
    background:
      radial-gradient(ellipse 30% 20% at 3% 4%, var(--cover-red) 0%, transparent 100%),
      radial-gradient(ellipse 22% 14% at 40% 66%, var(--cover-magenta) 0%, transparent 100%),
      radial-gradient(ellipse 16% 12% at 20% 72%, #f3eef6 0%, transparent 100%),
      radial-gradient(ellipse 50% 40% at 60% 40%, var(--cover-lavender) 0%, transparent 100%),
      linear-gradient(180deg, #4a1f3c 0%, var(--cover-violet) 35%, #3c3d6e 65%, var(--cover-navy) 88%);
  }
  .cover-art::after {
    content: "";
    position: absolute;
    right: 0;
    top: 300px;
    width: 405px;
    height: 635px;
    background: linear-gradient(160deg, #1b2140 0%, #0b0f26 60%);
    border-radius: 60% 0 0 0;
    opacity: 0.85;
  }
  .tagline {
    position: absolute;
    top: 80px;
    left: 0;
    right: 0;
    text-align: center;
    font-family: "Questrial", sans-serif;
    font-size: 17px;
    letter-spacing: 0.3px;
    margin: 0;
  }
  .title {
    position: absolute;
    top: 122px;
    left: 0;
    right: 0;
    margin: 0;
    text-align: center;
    font-family: "Michroma", sans-serif;
    font-weight: 400;
    font-size: 92px;
    line-height: 1.2;
    letter-spacing: 2px;
  }
  .subtitle-band {
    position: absolute;
    left: 47px;
    top: 242px;
    width: 528px;
    height: 45px;
    background: var(--band-dark);
    display: flex;
    align-items: center;
    justify-content: center;
  }
  .subtitle {
    margin: 0;
    font-family: "Michroma", sans-serif;
    font-weight: 400;
    font-size: 23px;
    letter-spacing: 1px;
  }
  .series-line {
    position: absolute;
    top: 852px;
    left: 0;
    right: 0;
    margin: 0;
    text-align: center;
    font-family: "Questrial", sans-serif;
    font-size: 15px;
  }
  .author {
    position: absolute;
    top: 876px;
    left: 0;
    right: 0;
    margin: 0;
    text-align: center;
    font-family: "Michroma", sans-serif;
    font-size: 24px;
    letter-spacing: 1px;
  }
</style>
</head>
<body>
  <main class="stage">
    <section class="book-cover">
      <div class="cover-art" role="img" aria-label="Photograph seen from behind an officer firing a handgun toward a distant silhouette, lit by red, blue and white emergency lights in haze"></div>
      <p class="tagline">"It WILL happen, and it will come out of nowhere..."</p>
      <h1 class="title">R.K.T</h1>
      <div class="subtitle-band">
        <h2 class="subtitle">Beyond the Silence Fell</h2>
      </div>
      <p class="series-line">One Law Enforcement Family...Three Life-Changing Stories</p>
      <p class="author">Lt. Dan Morrow</p>
    </section>
  </main>
</body>
</html>
```